Business Card Design

Needing a business card design similar to the business card that is attached.

Industry/Entity Type

Business

Contact Information for Business Card

Design similar to the b-cards that is attached.

```html
<!DOCTYPE html>
<html lang="en">
<head>
<meta charset="utf-8">
<title>Business Card – Trim &amp; Safe Margin</title>
<link rel="stylesheet" href="https://fonts.googleapis.com/css2?family=Patrick+Hand+SC&display=swap">
<style>
  :root {
    --paper: #ffffff;
    --trim-red: #e00000;
    --guide-cyan: #33e6ee;
    --ink: #111111;
    --art-cyan: #3fe8f0;
    --art-cyan-soft: #bff6fa;
    --art-red: #e8101c;
    --art-violet: #a898ec;
    --art-orange: #ff7a20;
    --art-green: #30d030;
  }
  html, body {
    margin: 0;
    padding: 0;
    width: 1200px;
    height: 707px;
    overflow: hidden;
    background: var(--paper);
  }
  .card {
    display: block;
    width: 1200px;
    height: 707px;
  }
  .trim-line { fill: none; stroke: var(--trim-red); stroke-width: 3; }
  .guide-line { fill: none; stroke: var(--guide-cyan); stroke-width: 3.5; stroke-dasharray: 7 6; }
  .contact-label,
  .contact-value {
    font-family: "Patrick Hand SC", cursive;
    font-size: 25px;
    fill: var(--ink);
    letter-spacing: 1.5px;
  }
</style>
</head>
<body>
<svg class="card" viewBox="0 0 1200 707" xmlns="http://www.w3.org/2000/svg" aria-label="Business card">
  <defs>
    <linearGradient id="trim-art-fill" x1="0" y1="0" x2="0" y2="1">
      <stop offset="0" stop-color="var(--art-cyan-soft)"/>
      <stop offset="1" stop-color="var(--art-cyan)"/>
    </linearGradient>
    <linearGradient id="margin-art-fill" x1="0" y1="0" x2="1" y2="0">
      <stop offset="0" stop-color="var(--art-red)"/>
      <stop offset=".35" stop-color="var(--art-violet)"/>
      <stop offset=".65" stop-color="var(--art-orange)"/>
      <stop offset="1" stop-color="var(--art-green)"/>
    </linearGradient>
  </defs>

  <rect class="trim-line" x="2" y="2" width="1196" height="703"/>

  <g class="guides">
    <path class="guide-line" d="M565 234 V570 H787"/>
    <path class="guide-line" d="M124 418 H565"/>
  </g>

  <rect class="trim-art" role="img" aria-label="Hand-lettered word TRIM in cyan with a dripping letter"
        x="363" y="138" width="164" height="154" rx="10" fill="url(#trim-art-fill)" opacity=".55"/>

  <rect class="safe-margin-art" role="img" aria-label="Hand-lettered words SAFE MARGIN in tumbling multicoloured letters"
        x="121" y="295" width="420" height="104" rx="10" fill="url(#margin-art-fill)" opacity=".45"/>

  <g class="contact">
    <text class="contact-label" x="613" y="360">Tel:</text>
    <text class="contact-value" x="795" y="360">********</text>
    <text class="contact-label" x="613" y="404">Website:</text>
    <text class="contact-value" x="795" y="404">&amp;&amp;***&amp;***&amp;**&amp;*</text>
    <text class="contact-label" x="613" y="486">Address:</text>
    <text class="contact-value" x="795" y="486">***&amp;****&amp;** **&amp;****&amp;*</text>
    <text class="contact-label" x="613" y="535">Email:</text>
    <text class="contact-value" x="795" y="535">*********@**.com</text>
  </g>
</svg>
</body>
</html>
```